Lumen Business Cards

We need a new look business cvard to refelect our new look website www.lumenplan.com.au
We’re Lumen, a team of town planning and traffic and transport engineering specialists located in Melbourne.

Lumen is a company that is structured, articulate, dynamic, progressive, accurate and adaptable.
Our key messages are:
1. We make your life easier by doing what we do best
2. We tell you what you need to know not what you want to hear
3. Polished and professional but not afraid to show some personality

we would like a bold new look that is polished and professional but not afraid to show a bit of personality

Target Market(s)

Lumen’s diverse client base consists of architecture practices, builders, developers, local government and the legal fraternity.

Industry/Entity Type

Town

Requirements
Must have
• must use our logo and have the following information

Joel Petrakis
Director

Lumen Advisory Pty Ltd
Hillgate first floor
Cotter Street
Kewdale VIC 3187 Australia
+61 03 9581 6724
mail@lumenplan.com.au
www.lumenplan.com.au
Nice to have
• We would like to see the logo used or the colours of the logo used.

```html
<!DOCTYPE html>
<html lang="en">
<head>
<meta charset="utf-8">
<title>Lumen Business Cards</title>
<link href="https://fonts.googleapis.com/css2?family=Roboto:wght@300;400;700&display=swap" rel="stylesheet">
<style>
  :root {
    --backdrop: #e9e7e3;
    --card-white: #f4f4f3;
    --card-border: #d9dadb;
    --panel: #efefee;
    --frame-blue: #4a8fc4;
    --name-blue: #4b8fc1;
    --brand-green: #59a86b;
    --ink: #6d737a;
    --ink-strong: #5a6169;
    --rule: #8b9096;
    --white: #ffffff;
  }
  * { box-sizing: border-box; margin: 0; padding: 0; }
  html, body {
    width: 1200px; height: 900px; overflow: hidden;
    background: var(--backdrop);
    font-family: "Roboto", Helvetica, Arial, sans-serif;
  }
  .canvas {
    position: relative; width: 1200px; height: 900px;
  }
  .card {
    position: absolute; left: 280px;
    width: 640px; height: 366px;
    box-shadow: 0 6px 18px rgba(0,0,0,0.12);
  }
  .card--front { top: 60px; background: var(--card-white); }
  .card--back  { top: 474px; background: var(--card-border); }

  /* front */
  .front-frame {
    position: absolute; inset: 16px;
    border: 2px solid var(--frame-blue);
  }
  .front-logo {
    position: absolute; left: 0; right: 0; top: 140px;
    display: flex; align-items: center; justify-content: center; gap: 18px;
  }
  .brand-mark {
    width: 34px; height: 34px; background: var(--frame-blue);
  }
  .brand-name {
    font-weight: 400; font-size: 62px; letter-spacing: 1px;
    color: var(--ink-strong); line-height: 1;
  }

  /* back */
  .back-panel {
    position: absolute; inset: 14px;
    background: var(--panel);
  }
  .name-block {
    position: absolute; left: 380px; top: 14px;
    width: 240px; height: 150px;
    background: var(--name-blue); color: var(--white);
    display: flex; flex-direction: column; align-items: center; justify-content: center;
    text-align: center;
  }
  .name-block .person {
    font-weight: 300; font-size: 22px; letter-spacing: 0.5px; text-transform: uppercase;
  }
  .name-block .role {
    font-weight: 300; font-size: 13px; margin-top: 4px;
  }
  .brand-block {
    position: absolute; left: 468px; top: 164px;
    width: 158px; height: 160px;
    background: var(--brand-green);
    display: flex; align-items: center; justify-content: center;
  }
  .brand-block .brand-name {
    color: var(--white); font-weight: 300; font-size: 46px;
  }
  .contact {
    position: absolute; right: 288px; top: 60px;
    width: 300px; text-align: right;
    color: var(--ink); font-weight: 300; font-size: 15px; line-height: 1.5;
  }
  .contact .rule {
    height: 1px; background: var(--rule); margin: 12px 0 12px 40px;
  }
  .website {
    position: absolute; left: 250px; width: 200px; top: 290px;
    text-align: right;
    font-weight: 700; font-size: 15px; color: var(--ink-strong);
  }
</style>
</head>
<body>
<main class="canvas">
  <section class="card card--front" aria-label="Business card front">
    <div class="front-frame"></div>
    <div class="front-logo">
      <span class="brand-mark"></span>
      <span class="brand-name">lumen</span>
    </div>
  </section>

  <section class="card card--back" aria-label="Business card back">
    <div class="back-panel"></div>
    <div class="name-block">
      <span class="person">Joel Petrakis</span>
      <span class="role">Director</span>
    </div>
    <div class="brand-block">
      <span class="brand-name">lumen</span>
    </div>
    <div class="contact">
      <p>+61 03 9581 6724</p>
      <p>mail@lumenplan.com.au</p>
      <div class="rule"></div>
      <p>Lumen Advisory Pty Ltd</p>
      <p>Hillgate first floor, Cotter Street</p>
      <p>Kewdale VIC 3187 Australia</p>
      <div class="rule"></div>
    </div>
    <p class="website">www.lumenplan.com.au</p>
  </section>
</main>
</body>
</html>
```